OLU58 biz card & Stationery

LU58 is a personalized shopping experience brought to you, that lets you find and discover fashion goods through a collection of boutiques curated by taste-makers - celebrities, stylists, designers, and fashion bloggers. Boutiques uses visual technology to help fashionistas discover and shop their look and creates the opportunity for designers to showcase their collections and latest inspirations online.

OLU58 is built on technology developed by our team of fashion experts who work with engineers to “teach” our computer systems to understand various patterns, pairings, and genre definitions. When signed into your account, OLU58 learns about your style and preferences and in turn, provides you better results and recommendations over time. Ultimately, OLU58 will provide shoppers with a much richer and interactive shopping experience and help drive traffic to retailers' websites.

We need a definitely cool business card. The card must be black! And must use our official logo which can be download from OLU58.com

The address for Letter head and evenlop, please use 4872 Crestwick Parkway, Sutie 510 Los Angeles CA90412, email will be anyone@OLU58.com, website is www.OLU58.com

thanks

We received some of the design, thanks. But most of the design are not what we want. We need a very clean version with black ground, you may also use some dark gray to add the element. please take a look at http://morvalstudio.no/work/#pelter__ostrama/, we do like this kind of design very much. hope it help.

```html
<!DOCTYPE html>
<html lang="en">
<head>
<meta charset="utf-8">
<title>OLU58 Envelope</title>
<link rel="stylesheet" href="https://fonts.googleapis.com/css2?family=PT+Sans+Narrow:wght@700&family=Lato:wght@400&display=swap">
<style>
  :root {
    --ink: #000000;
    --paper: #ffffff;
    --accent-gray: #4a4a4a;
    --label: #222222;
  }
  html, body {
    margin: 0;
    padding: 0;
    width: 1200px;
    height: 900px;
    overflow: hidden;
    background: var(--paper);
  }
  .stage {
    position: relative;
    width: 1200px;
    height: 900px;
    background: var(--paper);
  }
  .envelope-flap {
    position: absolute;
    left: 150px;
    top: 174px;
    width: 902px;
    height: 102px;
  }
  .envelope-flap svg { display: block; }
  .flap-brand {
    position: absolute;
    left: 262px;
    top: 184px;
    width: 190px;
    transform: rotate(180deg);
    color: var(--paper);
  }
  .envelope-body {
    position: absolute;
    left: 150px;
    top: 279px;
    width: 902px;
    height: 445px;
    box-sizing: border-box;
    border: 3px solid var(--ink);
    background: var(--paper);
  }
  .footer-band {
    position: absolute;
    left: 0;
    right: 0;
    bottom: 0;
    height: 94px;
    background: var(--ink);
    color: var(--paper);
  }
  .accent-bar {
    position: absolute;
    width: 15px;
    background: var(--accent-gray);
  }
  .accent-bar--flap { left: 671px; top: 2px; height: 100px; }
  .accent-bar--band { left: 668px; top: 0; height: 64px; }
  .brand-name {
    font-family: "Lato", sans-serif;
    font-weight: 400;
    font-size: 46px;
    line-height: 1;
    letter-spacing: 0.02em;
    margin: 0;
  }
  .brand-tagline {
    font-family: "Lato", sans-serif;
    font-weight: 400;
    font-size: 11px;
    letter-spacing: 0.12em;
    margin: 6px 0 0 2px;
    white-space: nowrap;
  }
  .band-brand {
    position: absolute;
    left: 29px;
    top: 12px;
  }
  .sender-address {
    position: absolute;
    right: 22px;
    top: 19px;
    font-family: "PT Sans Narrow", sans-serif;
    font-weight: 700;
    font-style: normal;
    font-size: 12.5px;
    line-height: 20px;
    text-align: right;
    word-spacing: 0.12em;
  }
  .piece-label {
    position: absolute;
    left: 0;
    width: 1200px;
    top: 836px;
    text-align: center;
    font-family: "Lato", sans-serif;
    font-size: 26px;
    color: var(--label);
    margin: 0;
  }
</style>
</head>
<body>
<div class="stage">
  <div class="envelope-flap">
    <svg width="902" height="102" viewBox="0 0 902 102" aria-hidden="true">
      <path d="M0 102 L0 88 Q0 70 18 54 L60 16 Q76 2 100 2 L802 2 Q826 2 842 16 L884 54 Q902 70 902 88 L902 102 Z" fill="var(--ink)"/>
    </svg>
    <div class="accent-bar accent-bar--flap"></div>
  </div>
  <div class="flap-brand">
    <p class="brand-name">OLU58</p>
    <p class="brand-tagline">CURATED STYLE BOUTIQUES</p>
  </div>

  <div class="envelope-body">
    <div class="footer-band">
      <div class="band-brand">
        <p class="brand-name">OLU58</p>
        <p class="brand-tagline">CURATED STYLE BOUTIQUES</p>
      </div>
      <div class="accent-bar accent-bar--band"></div>
      <address class="sender-address">
        4872 Crestwick Parkway,<br>
        Sutie 510 Los Angeles CA90412<br>
        www.OLU58.com
      </address>
    </div>
  </div>

  <p class="piece-label">envelope</p>
</div>
</body>
</html>
```